Rex Calloway-themed e-vite for my dad's 75th birthday party

Hi,
My sister and I are throwing a huge birthday bash for my dad's 75th birthday and the theme is Rex Calloway ( with a touch of Percy Vantage)!

I want a fun invitation to send to all our friends via email.

Here is my idea for the text (but I'm open to other ideas).

Thank you!

-----------------

The Crown's Hidden Bureau invites you to Gordy's 75th Birthday.

At 2913 Larchfield Crescent, Vancouver

On Saturday, August 8
4 pm - 10 pm

A Thousand Quiet Nights... so RSVP by July 20 before you Fall Before Dawn and let us know if only the Spy in the Silver Coat could keep you away.

This is your mission, should you choose to accept it.

RSVP to Miss Quillworth at mtorvald@pelmar.ca

Dress with a touch of Calloway, Rex Calloway.

---------------------

Target Market(s)

My dad's friends (mostly 50-80 years old). And my friends (30s). All live in vancouver, Canada. Most are of British ancestry.

Requirements
Must have
• + Fun Rex Calloway/Percy vantage design. Prefer something retro 60s looking.
• + Date, address, time rsvp info.
• + Must be the right dimensions, size and format for me to easily email.
• + Should be PORTRAIT orientation (not landscape) as I find this better for email.
Nice to have
• I'd love a retro 60s theme that evokes Neil Harwick-era Rex Calloway, blended with a bit of Percy Vantage, blended with a bit of Glass Desks.
• I found this design online which I copied the text from.
• http://brightfetedesigns.com/rex-calloway-theme-party/
• I would like my invite to be better designed and be a bit more fun.
• I am very open to different suggestions for the text.
Should not have
• The only Rex Calloway we like is Neil Harwick! I don't want to see Clive Dunmore, Walter Fenn or any of the other Calloways!

```html
<!DOCTYPE html>
<html lang="en">
<head>
<meta charset="utf-8">
<title>Gordy's 75th Birthday – Invitation</title>
<link rel="stylesheet" href="https://fonts.googleapis.com/css2?family=Source+Sans+3:wght@400;600;700&display=swap">
<style>
  :root {
    --page: #ffffff;
    --card: #a89f93;
    --card-light: #b6aea3;
    --ink: #2a2521;
    --accent: #8b2126;
    --figure: #2b2623;
  }
  * { margin: 0; padding: 0; box-sizing: border-box; }
  html, body {
    width: 1200px;
    height: 1002px;
    overflow: hidden;
    background: var(--page);
  }
  body {
    position: relative;
    font-family: "Source Sans 3", "Myriad Pro", Arial, sans-serif;
    color: var(--ink);
  }
  .invite {
    position: absolute;
    left: 377px;
    top: 237px;
    width: 435px;
    height: 562px;
    background: var(--card);
    overflow: hidden;
  }
  .invite__backdrop {
    position: absolute;
    left: -60px;
    top: -150px;
    width: 560px;
    height: 560px;
  }
  .invite__text {
    position: absolute;
    line-height: 1;
    white-space: nowrap;
  }
  .invite__host {
    left: 23px;
    top: 24px;
    font-size: 26px;
    font-weight: 700;
    letter-spacing: 0.2px;
  }
  .invite__figure {
    position: absolute;
    left: 26px;
    top: 62px;
    width: 171px;
    height: 202px;
  }
  .invite__lead {
    left: 220px;
    top: 62px;
    font-size: 18px;
    font-weight: 700;
  }
  .invite__guest {
    left: 220px;
    top: 95px;
    font-size: 26px;
    font-weight: 700;
  }
  .invite__occasion {
    left: 220px;
    top: 132px;
    font-size: 26px;
    font-weight: 700;
    color: var(--accent);
  }
  .invite__address {
    left: 31px;
    top: 287px;
    font-size: 17px;
    font-weight: 700;
  }
  .invite__date {
    left: 31px;
    top: 317px;
    font-size: 20px;
    font-weight: 700;
    color: var(--accent);
  }
  .invite__time {
    left: 31px;
    top: 342px;
    font-size: 20px;
    font-weight: 700;
    color: var(--accent);
  }
  .invite__rsvp-note {
    position: absolute;
    left: 118px;
    top: 372px;
    width: 300px;
    font-size: 12.5px;
    font-weight: 700;
    line-height: 1.3;
    text-align: center;
    transform: rotate(-6deg);
    transform-origin: center;
  }
  .invite__mission {
    left: 13px;
    top: 462px;
    font-size: 17px;
    font-weight: 700;
    color: var(--accent);
  }
  .invite__contact,
  .invite__dress {
    left: 13px;
    font-size: 14px;
    font-weight: 400;
  }
  .invite__contact { top: 506px; }
  .invite__dress { top: 530px; }
</style>
</head>
<body>
  <main class="invite">
    <svg class="invite__backdrop" viewBox="0 0 560 560" role="img" aria-label="Spiral gun-barrel backdrop pattern">
      <defs>
        <radialGradient id="barrel-glow" cx="50%" cy="50%" r="50%">
          <stop offset="0%" stop-color="var(--card)" stop-opacity="0"/>
          <stop offset="55%" stop-color="var(--card-light)" stop-opacity="0.55"/>
          <stop offset="100%" stop-color="var(--card)" stop-opacity="0"/>
        </radialGradient>
      </defs>
      <rect width="560" height="560" fill="url(#barrel-glow)"/>
    </svg>

    <h1 class="invite__text invite__host">THE CROWN'S HIDDEN BUREAU</h1>

    <svg class="invite__figure" viewBox="0 0 171 202" role="img" aria-label="Illustration of a secret agent in a tuxedo holding a pistol">
      <rect width="171" height="202" rx="6" fill="var(--figure)"/>
    </svg>

    <p class="invite__text invite__lead">INVITES YOU TO</p>
    <p class="invite__text invite__guest">GORDY'S</p>
    <p class="invite__text invite__occasion">75th BIRTHDAY.</p>

    <p class="invite__text invite__address">At 2913 Larchfield Crescent, Vancouver</p>
    <p class="invite__text invite__date">On Saturday, August 8</p>
    <p class="invite__text invite__time">4 pm - 10 pm</p>

    <p class="invite__rsvp-note">A Thousand Quiet Nights... so RSVP by July 20 before you Fall Before Dawn and let us know if only the Spy in the Silver Coat could keep you away.</p>

    <p class="invite__text invite__mission">This is your mission, should you choose to accept it.</p>

    <p class="invite__text invite__contact">RSVP to Miss Quillworth at mtorvald@pelmar.ca</p>
    <p class="invite__text invite__dress">Dress with a touch of Calloway, Rex Calloway.</p>
  </main>
</body>
</html>
```